8.5 x 8.5 - HELOC Product Campaign

Home Equity Lines of Credit
are BACK!!!

* Up to 97.5% on Owner Occupied Properties
* 700 Minimum Scores
* Fund in only 2-3 weeks

Can be used for...
* Education Expense
* Bill Consolidation
* Home Improvement
* Investments

Call today for more information!
(800) 417-2960

Bluegate Lending Partners, Inc.
NMLS #381760
www.bluegatelendhub.com

```html
<!DOCTYPE html>
<html lang="en">
<head>
<meta charset="utf-8">
<title>Bluegate Lending Partners – HELOC Campaign</title>
<link rel="stylesheet" href="https://fonts.googleapis.com/css2?family=Oswald:wght@300;400;500;600&family=Source+Sans+3:wght@400;600;700&display=swap">
<style>
  :root {
    --blue: #1a5aa6;
    --gold: #c8b43a;
    --gold-soft: #d6c65e;
    --gold-edge: #e8dc94;
    --ink: #333333;
    --paper: #ffffff;
    --backdrop: #e4e4e4;
  }
  * { box-sizing: border-box; margin: 0; padding: 0; }
  html, body { width: 1200px; height: 1140px; overflow: hidden; background: var(--backdrop); }
  .flyer {
    position: absolute; left: 50px; top: 20px;
    width: 1100px; height: 1100px;
    background: var(--paper); overflow: hidden;
  }
  .hero-photo {
    position: absolute; left: 200px; top: 138px; width: 900px; height: 715px;
    background:
      linear-gradient(90deg, #ffffff 0%, rgba(255,255,255,0.95) 22%, rgba(255,255,255,0) 55%),
      linear-gradient(180deg, rgba(255,255,255,0.9) 0%, rgba(255,255,255,0) 30%),
      linear-gradient(135deg, #efe6dc 0%, #d8c3ad 40%, #8a6a52 70%, #5b4a44 100%);
  }
  .headline {
    position: absolute; left: 49px; top: 65px;
    font-family: "Oswald", sans-serif; font-weight: 600;
    font-size: 58px; line-height: 88px; color: var(--blue);
    letter-spacing: -0.8px;
  }
  .headline-rule {
    position: absolute; left: 49px; top: 274px; width: 268px; height: 3px;
    background: var(--gold);
  }
  .features { position: absolute; left: 58px; top: 335px; list-style: none; }
  .features li {
    display: flex; align-items: center; gap: 14px; height: 45px;
    font-family: "Oswald", sans-serif; font-weight: 300; font-size: 34px; color: var(--blue);
  }
  .features svg { width: 24px; height: 24px; flex: none; }
  .uses-title {
    position: absolute; left: 49px; top: 598px; line-height: 50px;
    font-family: "Oswald", sans-serif; font-weight: 500; font-size: 38px; color: var(--gold);
  }
  .use-tile { position: absolute; top: 677px; width: 243px; height: 180px; }
  .use-photo {
    width: 243px; height: 179px; border: 2px solid var(--gold); border-radius: 10px 10px 0 0;
  }
  .use-label {
    position: absolute; left: 10px; top: 126px; width: 222px; height: 50px;
    border-radius: 25px; background: var(--gold); border: 2px solid var(--gold-edge);
    display: flex; align-items: center; justify-content: center;
    font-family: "Source Sans 3", sans-serif; font-size: 21px; color: #ffffff;
  }
  .cta {
    position: absolute; left: 52px; top: 915px; width: 1000px; height: 50px;
    border-radius: 25px; background: var(--gold); border: 2px solid var(--gold-edge);
  }
  .cta-text {
    position: absolute; left: 51px; top: 0; line-height: 46px;
    font-family: "Oswald", sans-serif; font-weight: 400; font-size: 33px; color: #ffffff;
  }
  .cta-phone {
    position: absolute; right: -2px; top: -2px; width: 418px; height: 50px;
    border-radius: 25px; background: var(--blue); border: 2px solid var(--gold-edge);
    display: flex; align-items: center; justify-content: center; gap: 12px;
    font-family: "Oswald", sans-serif; font-weight: 400; font-size: 33px; color: var(--gold-soft);
  }
  .cta-phone svg { width: 28px; height: 28px; }
  .brand {
    position: absolute; left: 770px; top: 100px; display: flex; align-items: center; gap: 12px;
  }
  .brand-dot { width: 44px; height: 44px; border-radius: 50%; background: var(--gold); flex: none; }
  .brand-name {
    font-family: "Oswald", sans-serif; font-weight: 500; font-size: 28px; line-height: 34px;
    color: var(--blue); width: 230px;
  }
  .footer-legal {
    position: absolute; left: 49px; top: 1008px;
    font-family: "Source Sans 3", sans-serif; font-size: 18px; color: var(--ink);
  }
  .footer-legal span { margin-left: 18px; }
  .footer-address {
    position: absolute; left: 49px; top: 1042px;
    font-family: "Source Sans 3", sans-serif; font-size: 18px; color: var(--blue);
  }
  .footer-web {
    position: absolute; left: 452px; top: 1030px;
    font-family: "Source Sans 3", sans-serif; font-weight: 700; font-size: 30px; color: var(--blue);
  }
  .social { position: absolute; left: 866px; top: 1027px; display: flex; gap: 18px; }
  .social span { width: 34px; height: 34px; border-radius: 50%; background: var(--gold); display: block; }
</style>
</head>
<body>
<main class="flyer">
  <div class="hero-photo" role="img" aria-label="Couple sitting on a sofa looking at a tablet among moving boxes"></div>

  <div class="brand">
    <span class="brand-dot"></span>
    <span class="brand-name">Bluegate Lending Partners, Inc.</span>
  </div>

  <h1 class="headline">Home Equity Lines of Credit<br>are BACK!!!</h1>
  <div class="headline-rule"></div>

  <ul class="features">
    <li><svg viewBox="0 0 24 24"><circle cx="12" cy="12" r="9" fill="none" stroke="#c8b43a" stroke-width="2"/><path d="M7.5 12.5l3 3 6-7" fill="none" stroke="#1a5aa6" stroke-width="2.4" stroke-linecap="round" stroke-linejoin="round"/></svg>Up to 97.5% on Owner Occupied Properties</li>
    <li><svg viewBox="0 0 24 24"><circle cx="12" cy="12" r="9" fill="none" stroke="#c8b43a" stroke-width="2"/><path d="M7.5 12.5l3 3 6-7" fill="none" stroke="#1a5aa6" stroke-width="2.4" stroke-linecap="round" stroke-linejoin="round"/></svg>700 Minimum Scores</li>
    <li><svg viewBox="0 0 24 24"><circle cx="12" cy="12" r="9" fill="none" stroke="#c8b43a" stroke-width="2"/><path d="M7.5 12.5l3 3 6-7" fill="none" stroke="#1a5aa6" stroke-width="2.4" stroke-linecap="round" stroke-linejoin="round"/></svg>Fund in only 2-3 weeks</li>
  </ul>

  <h2 class="uses-title">CAN BE USED FOR...</h2>

  <div class="use-tile" style="left:48px">
    <div class="use-photo" role="img" aria-label="Graduate in cap and gown" style="background:linear-gradient(160deg,#c9c4bd,#3a3f5a 70%,#1f2438)"></div>
    <div class="use-label">Education Expense</div>
  </div>
  <div class="use-tile" style="left:299px">
    <div class="use-photo" role="img" aria-label="Worried couple reviewing bills" style="background:linear-gradient(160deg,#e8e2dc,#b49a86 55%,#5a4a44)"></div>
    <div class="use-label">Bill Consolidation</div>
  </div>
  <div class="use-tile" style="left:551px">
    <div class="use-photo" role="img" aria-label="Couple planning a home improvement project" style="background:linear-gradient(160deg,#f1ece8,#c9b4c4 50%,#4d4a5e)"></div>
    <div class="use-label">Home Improvement</div>
  </div>
  <div class="use-tile" style="left:803px">
    <div class="use-photo" role="img" aria-label="Couple reviewing investment paperwork" style="background:linear-gradient(160deg,#f4efe9,#d9c6b0 50%,#6e5546)"></div>
    <div class="use-label">Investments</div>
  </div>

  <div class="cta">
    <span class="cta-text">CALL TODAY FOR MORE INFORMATION!</span>
    <div class="cta-phone">
      <svg viewBox="0 0 24 24"><path fill="#d6c65e" d="M6.6 10.8c1.4 2.8 3.8 5.1 6.6 6.6l2.2-2.2c.3-.3.7-.4 1-.2 1.1.4 2.3.6 3.6.6.6 0 1 .4 1 1V20c0 .6-.4 1-1 1C10.6 21 3 13.4 3 4c0-.6.4-1 1-1h3.5c.6 0 1 .4 1 1 0 1.3.2 2.5.6 3.6.1.3 0 .7-.2 1z"/></svg>
      (800) 417-2960
    </div>
  </div>

  <p class="footer-legal">Bluegate Lending Partners, Inc.<span>NMLS #381760</span></p>
  <p class="footer-address">2750 Harbor Mill Road, Columbia, MD 21046</p>
  <p class="footer-web">www.bluegatelendhub.com</p>
  <div class="social"><span></span><span></span><span></span></div>
</main>
</body>
</html>
```